Chiropractor needs a snazzy business card

Business card for a chiropractic office.
Office treats patients of all ages.
Focus is on a natural lifestyle.
Colors can include the logo colors as well as white and a little orange.
Ideally the card would have something chiropractic related such as a spine.

The back of the card should have a items for making appointments (date, times....)

```html
<!DOCTYPE html>
<html lang="en">
<head>
<meta charset="utf-8">
<title>Meridian Chiropractic – Business Card</title>
<link href="https://fonts.googleapis.com/css2?family=Questrial&display=swap" rel="stylesheet">
<style>
  :root {
    --backdrop: #e9e9e9;
    --card-black: #070707;
    --card-paper: #f4f4f2;
    --navy: #123d6b;
    --green: #4ea52f;
    --field-grey: #cfd0d8;
    --field-grey-light: #e3e4ea;
    --label-navy: #2a3f63;
    --notes-green: #dde9d4;
    --white: #ffffff;
  }
  * { margin: 0; padding: 0; box-sizing: border-box; }
  html, body {
    width: 1200px; height: 1000px; overflow: hidden;
    background: var(--backdrop);
    font-family: "Questrial", "Century Gothic", sans-serif;
  }
  .sheet {
    position: relative; width: 1200px; height: 1000px;
    display: flex; flex-direction: column; align-items: center; justify-content: center; gap: 60px;
  }
  .card {
    position: relative; width: 700px; height: 400px; overflow: hidden;
    box-shadow: 0 6px 18px rgba(0,0,0,0.18);
  }

  /* Front */
  .card-front { background: var(--card-black); }
  .spine-xray {
    position: absolute; left: 0; top: 0; width: 420px; height: 400px;
    background: radial-gradient(ellipse at 40% 45%, #b9b9b9 0%, #6e6e6e 30%, #2a2a2a 60%, #070707 85%);
  }
  .band { position: absolute; left: 0; width: 100%; }
  .band-navy { top: 300px; height: 22px; background: var(--navy); }
  .band-green { top: 322px; height: 30px; background: var(--green); }
  .logo-panel {
    position: absolute; left: 420px; top: 92px; width: 254px; height: 112px;
    background: var(--card-paper);
    display: flex; flex-direction: column; align-items: center; justify-content: center;
  }
  .brand-name {
    color: var(--navy); text-transform: uppercase; text-align: center; line-height: 1.05;
    font-family: "Questrial", "Century Gothic", sans-serif; font-weight: 400;
  }
  .logo-panel .brand-name .line-1 { display: block; font-size: 34px; letter-spacing: 2px; }
  .logo-panel .brand-name .line-2 { display: block; font-size: 19px; letter-spacing: 3px; }
  .contact {
    position: absolute; right: 28px; top: 218px; text-align: right;
    color: var(--white); font-size: 19px; line-height: 1.22;
  }

  /* Back */
  .card-back { background: var(--card-paper); }
  .card-back .brand-name { position: absolute; right: 70px; top: 38px; }
  .card-back .brand-name .line-1 { display: block; font-size: 44px; letter-spacing: 3px; }
  .card-back .brand-name .line-2 { display: block; font-size: 25px; letter-spacing: 4px; }
  .field { position: absolute; left: 0; width: 320px; height: 58px; }
  .field-date { top: 150px; }
  .field-time { top: 218px; }
  .field .label-strip {
    position: absolute; left: 30px; top: 0; width: 150px; height: 28px;
    background: var(--field-grey-light); color: var(--label-navy);
    font-size: 15px; padding: 5px 10px;
  }
  .field .write-line {
    position: absolute; left: 30px; top: 28px; width: 290px; height: 16px;
    background: var(--field-grey);
  }
  .notes-frame {
    position: absolute; left: 430px; top: 232px; width: 290px; height: 150px;
    border: 16px solid var(--notes-green); border-right: none;
  }
  .notes-label {
    position: absolute; left: 470px; top: 282px; color: var(--label-navy); font-size: 15px;
  }
</style>
</head>
<body>
<main class="sheet">
  <section class="card card-front" aria-label="Business card front">
    <div class="spine-xray" role="img" aria-label="Side-view X-ray of a human neck and cervical spine"></div>
    <div class="band band-navy"></div>
    <div class="band band-green"></div>
    <div class="logo-panel">
      <div class="brand-name"><span class="line-1">Meridian</span><span class="line-2">Chiropractic</span></div>
    </div>
    <div class="contact">
      <p class="contact-name">Dr. Laura Bennett</p>
      <p class="contact-phone">phone 555-014-2273</p>
      <p class="contact-email">e-mail care@meridianchiro.com</p>
    </div>
  </section>

  <section class="card card-back" aria-label="Business card back, appointment reminder">
    <div class="brand-name"><span class="line-1">Meridian</span><span class="line-2">Chiropractic</span></div>
    <div class="field field-date"><span class="label-strip">date:</span><span class="write-line"></span></div>
    <div class="field field-time"><span class="label-strip">time:</span><span class="write-line"></span></div>
    <div class="notes-frame"></div>
    <p class="notes-label">notes:</p>
  </section>
</main>
</body>
</html>
```